real esate business card with company logo and name

we need a business card design for a real esate company

The company name is Walsh & Ortiz Pty Ltd, and we have our logo designed and will upload. We want classic or moden feel. Black or white background. looks more textured. Should include folowinginformations
Paul Walsh and Tara Ortiz
Sales Agents & Onsite Manager
p: 07 5948 2610
F: 07 5948 2795
M:0451 786 923
3/22 Marlow Crescent, BROOKHAVEN QLD 4170

We want this business card looks professonal. Thank you in advance.

Industry/Entity Type

Real Estate Agent

Contact Information for Business Card

Paul Walsh and Tara Ortiz
Onsite Manager & Sales Agents
p: 07 5948 2610
M:0451 786 923

Font styles to use
Serif

Colors
000000
fbfbfb
333333
959595

Requirements
Must have
• company logo and name, black or white back ground

```html
<!DOCTYPE html>
<html lang="en">
<head>
<meta charset="utf-8">
<title>Walsh &amp; Ortiz Pty Ltd – Business Card</title>
<link href="https://fonts.googleapis.com/css2?family=Lato:wght@400;700&family=Oswald:wght@300;400&display=swap" rel="stylesheet">
<style>
  :root {
    --page-bg: #e9e9e9;
    --card-light: #cbcbcb;
    --card-dark: #525357;
    --card-white: #fbfbfb;
    --divider: #ffffff;
    --ink-strong: #4a4a4a;
    --ink: #3a3a3a;
    --mark-grey: #8a8a8a;
    --name-grey: #959595;
  }
  * { margin: 0; padding: 0; box-sizing: border-box; }
  html, body { width: 1200px; height: 900px; overflow: hidden; }
  body {
    position: relative;
    background: var(--page-bg);
    font-family: "Lato", Arial, sans-serif;
  }
  .card {
    position: absolute;
    width: 556px;
    height: 344px;
    box-shadow: 0 6px 18px rgba(0,0,0,.12);
  }

  /* Contact side */
  .card-front {
    left: 238px; top: 61px;
    background: var(--card-light);
    overflow: hidden;
  }
  .front-dark-panel {
    position: absolute; top: 0; right: 0;
    width: 145px; height: 100%;
    background: var(--card-dark);
  }
  .front-divider {
    position: absolute; top: 0; left: 401px;
    width: 10px; height: 100%;
    background: var(--divider);
  }
  .agent-names {
    position: absolute; left: 41px; top: 36px;
    font-size: 20px; font-weight: 700; color: var(--ink-strong);
  }
  .agent-roles {
    position: absolute; left: 41px; top: 63px;
    font-size: 15px; color: var(--ink-strong);
  }
  .office-address {
    position: absolute; left: 41px; top: 180px;
    font-size: 15px; line-height: 19px; color: var(--ink);
    font-style: normal;
  }
  .contact-list {
    position: absolute; left: 41px; top: 232px;
    list-style: none; font-size: 15px; color: var(--ink);
  }
  .contact-list li { display: flex; align-items: center; height: 21px; }
  .contact-list svg { width: 12px; height: 12px; margin-right: 10px; fill: var(--ink); }

  .front-brand {
    position: absolute; left: 341px; top: 104px;
    width: 130px; height: 130px;
    background: var(--card-light);
    border: 6px solid var(--divider);
    display: flex; align-items: center; justify-content: center;
    text-align: center;
    font-size: 17px; font-weight: 700; line-height: 21px;
    color: var(--ink-strong);
  }

  /* Brand side */
  .card-back {
    left: 457px; top: 518px;
    width: 560px;
    background: var(--card-white);
  }
  .brand-square-back {
    position: absolute; left: 196px; top: 60px;
    width: 168px; height: 168px;
    background: var(--mark-grey);
  }
  .company-name {
    position: absolute; left: 0; top: 258px; width: 100%;
    text-align: center;
    font-family: "Oswald", "Arial Narrow", sans-serif;
    font-weight: 400; font-size: 29px; letter-spacing: 1.5px;
    color: var(--name-grey);
  }
</style>
</head>
<body>

  <section class="card card-front">
    <div class="front-dark-panel"></div>
    <div class="front-divider"></div>

    <h1 class="agent-names">Paul Walsh and Tara Ortiz</h1>
    <p class="agent-roles">Onsite Manager &amp; Sales Agents</p>

    <address class="office-address">
      3/22 Marlow Crescent,<br>BROOKHAVEN QLD 4170
    </address>

    <ul class="contact-list">
      <li>
        <svg viewBox="0 0 12 12" aria-hidden="true"><path d="M3 0h6a1 1 0 0 1 1 1v10a1 1 0 0 1-1 1H3a1 1 0 0 1-1-1V1a1 1 0 0 1 1-1zm0.5 1.5v8h5v-8z"/></svg>
        07 5948 2610
      </li>
      <li>
        <svg viewBox="0 0 12 12" aria-hidden="true"><path d="M1 4c0-2 2-3 5-3s5 1 5 3v1H8.5V4h-5v1H1zM3 5.5h6l2 2.5V11H1V8z"/></svg>
        0451 786 923
      </li>
    </ul>

    <div class="front-brand">Walsh<br>&amp; Ortiz</div>
  </section>

  <section class="card card-back">
    <div class="brand-square-back"></div>
    <p class="company-name">WALSH &amp; ORTIZ PTY LTD.</p>
  </section>

</body>
</html>
```